Business card for Tolvery Anesthesia LLC

This is for a business care for Tolvery Anesthesia LLC. Dr. Lisbeth Tolvery, CRNA, DNAP is the sole provider in the LLC. Business address is 4718 N Brackley Street,
Oakhaven, PA 17342
CRNA stands for certified registered nurse anesthetist
"Keeping you safe and comfortable"
I plan to give this business card to the patients that I provide anesthesia to.
Creative design that ties into Anesthesia. Calm soothing colors.

Target Market(s)

Business card for my patients.

Industry/Entity Type

Medicine

Contact Information for Business Card

Creative, professional, eye catching

Logo Text

Tolvery Anesthesia

Font styles to use
Serif
Script

Colors

Designer to choose colors to be used in the design.

Requirements
Must have
• Tolvery Anesthesia
• Dr. Lisbeth Tolvery, CRNA, DNAP
• tolvery.anesthesia@ quillmail.net
Nice to have
• "Keeping you safe and comfortable"
Should not have
• phone number

```html
<!DOCTYPE html>
<html lang="en">
<head>
<meta charset="utf-8">
<title>Tolvery Anesthesia — Business Card</title>
<link href="https://fonts.googleapis.com/css2?family=Varela+Round&display=swap" rel="stylesheet">
<style>
  :root {
    --stage: #000000;
    --card-white: #ffffff;
    --teal: #05a98a;
    --ocean: #0a86c6;
    --brand-blue: #1a7fc4;
    --brand-green: #14a88a;
    --ink-grey: #666a6e;
    --soft-grey: #8a8d90;
  }
  * { margin: 0; padding: 0; box-sizing: border-box; }
  html, body {
    width: 1200px; height: 1000px; overflow: hidden;
    background: var(--stage);
    font-family: "Varela Round", "Helvetica Neue", Arial, sans-serif;
  }
  .canvas { position: relative; width: 1200px; height: 1000px; }

  .card {
    position: absolute; left: 286px; width: 628px; height: 358px;
    border-radius: 40px; overflow: hidden;
  }
  .card--front { top: 113px; }
  .card--back { top: 506px; background: var(--card-white); }

  .front-backdrop {
    position: absolute; inset: 0;
    background: linear-gradient(180deg, var(--teal) 0%, #069aa6 50%, var(--ocean) 100%);
  }
  .front-brand {
    position: absolute; left: 0; right: 0; top: 186px;
    text-align: center; color: var(--card-white);
  }
  .front-brand__name { font-size: 32px; line-height: 40px; letter-spacing: 0.2px; }
  .front-brand__tagline { font-size: 14.5px; letter-spacing: 0.9px; margin-top: 2px; }

  .back-brand {
    position: absolute; left: 0; width: 314px; top: 192px; text-align: center;
  }
  .back-brand__name { font-size: 24px; line-height: 28px; color: var(--brand-blue); }
  .back-brand__tagline { font-size: 10.5px; letter-spacing: 0.6px; color: var(--ink-grey); margin-top: 2px; }

  .divider {
    position: absolute; left: 298px; top: 24px; width: 4px; height: 318px;
    background: linear-gradient(90deg, rgba(0,0,0,0.18), rgba(0,0,0,0));
    border-radius: 2px;
    -webkit-mask-image: linear-gradient(180deg, transparent, #000 20%, #000 80%, transparent);
            mask-image: linear-gradient(180deg, transparent, #000 20%, #000 80%, transparent);
  }

  .contact { position: absolute; left: 325px; top: 114px; }
  .contact__name { font-size: 22px; line-height: 26px; color: var(--brand-blue); }
  .contact__creds { font-size: 15px; color: var(--brand-green); margin-top: 2px; }
  .contact__list { list-style: none; margin-top: 18px; }
  .contact__item {
    display: flex; align-items: flex-start; gap: 6px;
    font-size: 15px; line-height: 21px; color: var(--ink-grey); margin-bottom: 6px;
  }
  .contact__icon { flex: none; margin-top: 3px; }
</style>
</head>
<body>
<main class="canvas">
  <section class="card card--front">
    <div class="front-backdrop" role="img" aria-label="Soft teal-to-blue gradient where a faint repeating letter pattern sits"></div>
    <div class="front-brand">
      <div class="front-brand__name">Tolvery Anesthesia</div>
      <div class="front-brand__tagline">KEEPING YOU SAFE AND COMFORTABLE</div>
    </div>
  </section>

  <section class="card card--back">
    <div class="back-brand">
      <div class="back-brand__name">Tolvery Anesthesia</div>
      <div class="back-brand__tagline">KEEPING YOU SAFE AND COMFORTABLE</div>
    </div>
    <div class="divider"></div>
    <div class="contact">
      <div class="contact__name">Dr. Lisbeth Tolvery</div>
      <div class="contact__creds">CRNA, DNAP</div>
      <ul class="contact__list">
        <li class="contact__item">
          <svg class="contact__icon" width="17" height="13" viewBox="0 0 17 13" aria-hidden="true">
            <rect x="0" y="0" width="17" height="13" rx="1.5" fill="var(--brand-blue)"/>
            <path d="M1.5 1.5 L8.5 7 L15.5 1.5" fill="none" stroke="#fff" stroke-width="1.4"/>
            <path d="M1.5 11.5 L6 6.5 M15.5 11.5 L11 6.5" fill="none" stroke="#fff" stroke-width="1.2"/>
          </svg>
          <span>tolvery.anesthesia@quillmail.net</span>
        </li>
        <li class="contact__item">
          <svg class="contact__icon" width="17" height="17" viewBox="0 0 17 17" aria-hidden="true">
            <path d="M8.5 0.5 C4.9 0.5 2.5 3 2.5 6.2 C2.5 10 8.5 16.5 8.5 16.5 C8.5 16.5 14.5 10 14.5 6.2 C14.5 3 12.1 0.5 8.5 0.5 Z" fill="var(--brand-blue)"/>
            <circle cx="8.5" cy="6.3" r="2.3" fill="#fff"/>
          </svg>
          <span>4718 N Brackley Street,<br>Oakhaven, PA 17342</span>
        </li>
      </ul>
    </div>
  </section>
</main>
</body>
</html>
```